Communication and Marketing agency needs a new presentation card

We are a group of communication and marketing agencies specialized in companies that are in the logistics and industrial sector. The head agency is TELVANO Grupo and the group consists of 4 agencies: TELVANO Media, TELVANO Digital, TELVANO Research and EnlazaPorImagen. We hace 4 offices in Spain (Madrid, Barcelona, Valencia and Murcia). We are looking for a clean and attractive design that transmits our experience, brand presence in the market and knowledge to those who receive the card.It has to maintain the colors of the logo that is attached.
Target Market(s)
logistics and industrial sector
Marketing department
Clean and attractive design

```html
<!DOCTYPE html>
<html lang="en">
<head>
<meta charset="utf-8">
<title>TELVANO Grupo – Business Card</title>
<link rel="stylesheet" href="https://fonts.googleapis.com/css2?family=Montserrat:wght@400;500;600&display=swap">
<style>
  :root {
    --bg: #3a3b3d;
    --card-white: #ffffff;
    --brand-red: #b41f24;
    --ink: #231f20;
    --text-grey: #58595b;
    --band-grey: #5f6062;
    --band-light: #e6e6e6;
    --white: #ffffff;
  }
  * { margin: 0; padding: 0; box-sizing: border-box; }
  html, body { width: 1200px; height: 900px; overflow: hidden; }
  body {
    background: var(--bg);
    font-family: "Montserrat", sans-serif;
    position: relative;
  }
  .card {
    position: absolute;
    width: 700px;
    height: 400px;
    border-radius: 30px;
    overflow: hidden;
    left: 250px;
  }
  /* Front */
  .card-front { top: 35px; background: var(--card-white); }
  .front-logo {
    position: absolute; left: 44px; top: 70px;
    font-size: 38px; font-weight: 500; letter-spacing: 1px;
    color: var(--brand-red);
    white-space: nowrap;
  }
  .agency-list {
    position: absolute; right: 40px; top: 40px;
    display: flex; gap: 26px;
    list-style: none;
    font-size: 12px; font-weight: 500; color: var(--text-grey);
    white-space: nowrap;
  }
  .agency-list li:last-child { color: var(--brand-red); }
  .name-rule {
    position: absolute; left: 230px; right: 40px; top: 190px;
    height: 1.5px; background: var(--text-grey);
  }
  .person-name {
    position: absolute; left: 44px; top: 166px;
    font-size: 28px; font-weight: 500; color: var(--brand-red);
    white-space: nowrap;
  }
  .person-role {
    position: absolute; left: 56px; top: 202px;
    font-size: 15px; color: var(--text-grey); letter-spacing: .5px;
  }
  .contact-list {
    position: absolute; left: 56px; top: 228px;
    list-style: none;
    font-size: 17px; color: var(--text-grey);
  }
  .contact-list li { display: flex; align-items: center; gap: 14px; height: 30px; }
  .contact-icon { width: 22px; height: 22px; flex: none; }
  .social-band {
    position: absolute; left: 0; right: 0; bottom: 0; height: 68px;
    background: var(--band-grey);
    border-top: 5px solid var(--band-light);
    display: flex; align-items: center;
    padding-left: 44px;
    color: var(--white); font-size: 18px;
  }
  .social-label { margin-right: 18px; }
  .social-dots { display: flex; gap: 12px; list-style: none; margin-right: 20px; }
  .social-dots li {
    width: 30px; height: 30px; border-radius: 50%;
    background: var(--brand-red);
  }
  .social-handle { font-size: 18px; }
  /* Back */
  .card-back { top: 465px; background: var(--brand-red); }
  .back-logo {
    position: absolute; left: 0; right: 0; top: 150px;
    text-align: center;
    font-size: 54px; font-weight: 500; letter-spacing: 2px;
    color: var(--ink);
    white-space: nowrap;
  }
  .back-url {
    position: absolute; left: 0; right: 0; bottom: 40px;
    text-align: center;
    font-size: 17px; color: var(--white); letter-spacing: .5px;
  }
</style>
</head>
<body>
  <section class="card card-front" aria-label="Card front">
    <div class="front-logo">TELVANO Grupo</div>
    <ul class="agency-list">
      <li>TELVANO Research</li>
      <li>TELVANO Digital</li>
      <li>TELVANO Media</li>
    </ul>
    <div class="person-name">Your Name</div>
    <div class="name-rule"></div>
    <div class="person-role">POSITION</div>
    <ul class="contact-list">
      <li>
        <svg class="contact-icon" viewBox="0 0 22 22"><circle cx="11" cy="11" r="11" fill="#b41f24"/><path d="M7.5 6.5l2 0 1 2.5-1.3 1a6 6 0 0 0 2.8 2.8l1-1.3 2.5 1 0 2c-4.5.5-8.5-3.5-8-8z" fill="#fff"/></svg>
        <span>+00 0000 000 000</span>
      </li>
      <li>
        <svg class="contact-icon" viewBox="0 0 22 22"><circle cx="11" cy="11" r="11" fill="#b41f24"/><rect x="6" y="7.5" width="10" height="7" fill="none" stroke="#fff" stroke-width="1.2"/><path d="M6 7.5l5 4 5-4" fill="none" stroke="#fff" stroke-width="1.2"/></svg>
        <span>info@telvanogrupo.com</span>
      </li>
      <li>
        <svg class="contact-icon" viewBox="0 0 22 22"><circle cx="11" cy="11" r="11" fill="#b41f24"/><path d="M11 17s-4-4.5-4-7.5a4 4 0 0 1 8 0c0 3-4 7.5-4 7.5z" fill="#fff"/><circle cx="11" cy="9.5" r="1.5" fill="#b41f24"/></svg>
        <span>Office Address</span>
      </li>
    </ul>
    <div class="social-band">
      <span class="social-label">Follow us</span>
      <ul class="social-dots" aria-label="Social profiles">
        <li></li><li></li><li></li><li></li><li></li>
      </ul>
      <span class="social-handle">@telvanogrupo</span>
    </div>
  </section>

  <section class="card card-back" aria-label="Card back">
    <div class="back-logo">TELVANO Grupo</div>
    <div class="back-url">www.telvanogrupo.com</div>
  </section>
</body>
</html>
```